Need web redesign for cybersecurity startup whose mission is to make robust cybersecurity protection

We need a web redesign for Velnastra, a cyber security startup. We already have a logo and website but we’re looking for a redesign to reflect the new messaging and positioning of the company – and to update our look with a more polished feel. We’re looking for clean, powerful, confident designs that easily communicate the problems within the cybersecurity space and how Velnastra is the answer to those problems.

We can have the long-scrolling stripe layout for the home page, but we don’t want a bunch of interior pages with the same long-scroll format. We’d like to do something a little different and easier to navigate.

Velnastra’s products simplify and automate cybersecurity defense so non-experts can successfully protect their information and focus on their business. Velnastra’s mission is to provide proactive cybersecurity protection that is easy to use, easy to implement and easy to afford. The designs should reflect this populist message as well as confidence and maybe a little irreverence. Additional key words to describe the company are: secure, protection, easy, everyone.

Velnastra offers multiple security products which can both be purchased directly from their site. They provide the world’s most widely used WAF rule set for Quellwarden as well as Velnastra Guarded Linux (VGL) and Velnastra Guarded Linux Kernels to protect Linux servers, IoT devices and Kestrabox containers.

Target Market(s)

IT leaders in small and mid-sized businesses, hosting providers, and enterprise dev ops, product and security groups

Industry/Entity Type

Security

Number of Pages Required

5+ page

Font styles to use
Serif
Sans Serif

Requirements
Must have
• - We can have the long-scrolling stripe layout for the home page, but we don’t want a bunch of interior pages with the same long-scroll format. We’d like to do something a little different and easier to navigate.
• - Clean, powerful, confident designs
• - Real imagery coupled with line designs
Nice to have
• Specific icons to be used for all marketing and web materials for each product:
• - Brindle Guard for Linux (BG/L)
• - QuellWarden Rules
• - Velnastra Guarded Linux Kernels
• - PRAVT - Commercial Support
• - Shielded OS for Kestrabox
• - Shielded Apps for Kestrabox
Should not have
• - No typical imagery for cybersecurity such as binary code, hooded figures, etc.

```html
<!DOCTYPE html>
<html lang="en">
<head>
<meta charset="utf-8">
<title>Velnastra — Linux Server Protection</title>
<link href="https://fonts.googleapis.com/css2?family=Montserrat:wght@600;700;800&family=Open+Sans:ital,wght@0,400;0,600;0,700;1,400&display=swap" rel="stylesheet">
<style>
:root{
  --red:#e5284a;
  --red-deep:#d21c3b;
  --ink:#1f1f1f;
  --text:#555;
  --muted:#888;
  --line:#e2e2e2;
  --white:#fff;
  --blue:#2196e8;
  --dark:#2a2d31;
}
*{box-sizing:border-box;margin:0;padding:0}
html,body{width:1200px;height:4557px;overflow:hidden}
body{font-family:"Open Sans",Arial,sans-serif;color:var(--text);background:var(--white);position:relative}
section,header,footer{position:relative;width:1200px;overflow:hidden}
.abs{position:absolute}
.heading{font-family:"Montserrat",Arial,sans-serif;font-weight:800;color:var(--ink);text-transform:uppercase;text-align:center;letter-spacing:.3px}

/* header */
.site-header{height:91px;background:var(--white);overflow:visible;z-index:5}
.brand{position:absolute;left:88px;top:-30px;width:190px;height:190px;border-radius:50%;background:var(--white);display:flex;align-items:center;justify-content:center;gap:8px;box-shadow:0 2px 6px rgba(0,0,0,.08)}
.brand-dot{width:16px;height:16px;border-radius:50%;background:var(--red)}
.brand-name{font-family:"Montserrat",sans-serif;font-weight:800;font-size:19px;color:var(--ink);letter-spacing:.5px}
.main-nav{position:absolute;right:100px;top:40px;display:flex;gap:30px;align-items:center;font-size:13px;font-weight:600;color:#333}
.main-nav .active{color:var(--red)}

/* hero */
.hero{height:457px}
.hero-photo{position:absolute;inset:0;background:linear-gradient(180deg,#56654a 0%,#36412c 40%,#262b21 75%,#3d3d38 100%)}
.play{position:absolute;width:74px;height:74px;border:3px solid var(--white);border-radius:50%;display:flex;align-items:center;justify-content:center}
.hero .play{left:563px;top:97px;background:rgba(0,0,0,.25)}
.hero-title{position:absolute;left:0;right:0;top:195px;font-size:44px;line-height:56px;color:var(--white);text-align:center}

/* intro */
.intro{height:370px}
.intro .heading{position:absolute;left:0;right:0;top:65px;font-size:25px}
.intro-text{position:absolute;left:225px;width:750px;top:120px;font-size:12.5px;line-height:24px;text-align:center;color:#666}
.pills{position:absolute;left:0;right:0;top:262px;display:flex;justify-content:center;gap:16px}
.pill{height:38px;padding:0 36px;border:2px solid var(--red);border-radius:20px;display:flex;align-items:center;font-family:"Montserrat",sans-serif;font-weight:700;font-size:12.5px;color:var(--red);text-transform:uppercase}

/* services */
.services{height:382px;background:linear-gradient(135deg,#ec3354 0%,var(--red) 50%,var(--red-deep) 100%)}
.services .heading{position:absolute;left:0;right:0;top:55px;font-size:25px;color:var(--white)}
.service{position:absolute;display:flex;gap:18px;width:340px}
.service svg{flex:none}
.service h3{font-family:"Open Sans",sans-serif;font-weight:700;font-size:15px;color:var(--white);margin:4px 0 6px}
.service p{font-size:11.5px;line-height:19px;color:rgba(255,255,255,.9)}

/* clients */
.clients{height:285px}
.clients .heading{position:absolute;left:0;right:0;top:62px;font-size:25px}
.client-row{position:absolute;left:98px;top:128px;display:flex;gap:13px}
.client{width:190px;height:90px;border:1px solid #cfcfcf;display:flex;align-items:center;justify-content:center}
.client span{width:120px;height:22px;border-radius:11px;background:#ececec}
.rule{position:absolute;left:98px;width:1004px;height:1px;background:var(--line)}

/* harden */
.harden{height:550px}
.harden .heading{position:absolute;left:0;right:0;top:58px;font-size:22px}
.checks{position:absolute;left:100px;top:128px;width:420px;list-style:none}
.checks li{position:relative;padding-left:30px;font-size:12px;line-height:26px;color:#666;margin-bottom:29px}
.checks li svg{position:absolute;left:0;top:5px}
.harden-video{position:absolute;left:563px;top:130px;width:538px;height:340px;background:linear-gradient(180deg,#4a5546,#2d332b 55%,#3b4238)}
.harden-video .play{left:232px;top:133px;background:rgba(0,0,0,.2)}

/* testimonials */
.testimonial{height:285px}
.testimonial-photo{position:absolute;inset:0}
.t1 .testimonial-photo{background:linear-gradient(120deg,#3b3f45,#2c3035 45%,#4a4e55 100%)}
.t2 .testimonial-photo{background:linear-gradient(120deg,#4a4441,#2a2826 50%,#3d3b3a 100%)}
.quote-mark{position:absolute;left:0;right:0;top:28px;text-align:center;font-family:Georgia,serif;font-size:120px;line-height:120px;color:var(--white);font-weight:700}
.quote{position:absolute;left:300px;width:600px;top:138px;text-align:center;font-size:12.5px;line-height:24px;color:var(--white);font-style:italic}
.cite{position:absolute;left:0;right:0;top:220px;text-align:center;font-size:14px;color:var(--white)}
.cite b{font-weight:700;font-style:normal}
.cite i{font-style:italic}
.arrow{position:absolute;top:125px}

/* containers */
.containers{height:250px}
.containers .heading{position:absolute;left:0;right:0;top:68px;font-size:23px}
.containers p{position:absolute;left:220px;width:760px;top:118px;text-align:center;font-size:12px;line-height:24px;color:#666}

/* customers */
.customers{height:355px}
.customers .heading{position:absolute;left:0;right:0;top:58px;font-size:23px}
.customer{position:absolute;top:138px;width:240px;margin-left:-120px;text-align:center}
.customer svg{display:block;margin:0 auto 20px}
.customer span{font-family:"Montserrat",sans-serif;font-weight:700;font-size:17px;color:var(--ink)}

/* blog */
.blog{height:655px}
.blog .heading{position:absolute;left:0;right:0;top:78px;font-size:23px}
.feature-card{position:absolute;left:98px;top:145px;width:507px;height:430px;border:1px solid var(--line)}
.feature-img{position:absolute;left:6px;top:6px;width:493px;height:330px;background:linear-gradient(135deg,#bfe0f2,#5aa6d8 50%,#2a6fa8)}
.feature-card h4{position:absolute;left:18px;top:356px;font-size:18px;font-weight:600;color:var(--ink)}
.meta{font-size:11.5px;color:#777;display:flex;gap:14px;align-items:center}
.meta i{display:inline-block;width:10px;height:10px;background:var(--red);border-radius:2px;margin-right:5px;vertical-align:-1px}
.feature-card .meta{position:absolute;left:18px;top:395px}
.post{position:absolute;left:628px;width:475px;height:125px}
.post-thumb{position:absolute;left:0;top:0;width:150px;height:125px}
.post h5{position:absolute;left:184px;top:0;font-size:15px;font-weight:600;color:var(--ink)}
.post .meta{position:absolute;left:184px;top:30px;gap:10px}
.post p{position:absolute;left:184px;top:58px;width:290px;font-size:11px;line-height:19px;color:#777}

/* tweet band */
.tweet{height:95px;background:var(--blue)}
.tweet-icon{position:absolute;left:98px;top:24px;width:46px;height:46px;border-radius:50%;background:var(--white);opacity:.95}
.tweet p{position:absolute;left:200px;top:24px;width:800px;font-size:12.5px;line-height:22px;color:var(--white)}

/* contact */
.contact{height:425px}
.contact .heading{position:absolute;left:0;right:0;top:60px;font-size:23px}
.contact h6{position:absolute;top:140px;font-size:15px;font-weight:600;color:var(--ink)}
.field{position:absolute;height:35px;border:1px solid #cfcfcf;font-size:10.5px;color:#999;padding:10px 10px;text-transform:uppercase}
.submit{position:absolute;left:622px;top:353px;width:80px;height:28px;border-radius:14px;background:var(--red);color:var(--white);font-size:11px;font-weight:700;display:flex;align-items:center;justify-content:center}
.info{position:absolute;left:782px;display:flex;gap:16px;align-items:center;font-size:11.5px;line-height:18px;color:#666;width:320px}
.info-icon{flex:none;width:34px;height:34px;border-radius:50%;border:1px solid #e4e4e4;display:flex;align-items:center;justify-content:center}
.socials{position:absolute;left:782px;top:362px;display:flex;gap:6px}
.socials span{width:26px;height:26px;border-radius:50%}

/* footer */
.site-footer{height:72px}
.site-footer p{position:absolute;left:0;right:0;top:28px;text-align:center;font-size:11px;color:#777}
</style>
</head>
<body>

<header class="site-header">
  <div class="brand"><span class="brand-dot"></span><span class="brand-name">VELNASTRA</span></div>
  <nav class="main-nav">
    <span class="active">HOME</span><span>ABOUT US</span><span>SERVICES</span><span>BLOG</span><span>RESOURCES</span><span>CONTACT US</span>
    <svg width="15" height="15" viewBox="0 0 16 16"><circle cx="6.5" cy="6.5" r="5" fill="none" stroke="#333" stroke-width="2"/><line x1="10.5" y1="10.5" x2="15" y2="15" stroke="#333" stroke-width="2.4"/></svg>
  </nav>
</header>

<section class="hero">
  <div class="hero-photo" role="img" aria-label="Motorcyclist riding along a road through a dense green forest at dusk"></div>
  <div class="play"><svg width="26" height="28" viewBox="0 0 26 28"><path d="M4 2 L24 14 L4 26 Z" fill="#fff"/></svg></div>
  <h1 class="hero-title heading">Don’t be the next cyber victim.<br>Harden your shell now.</h1>
</section>

<section class="intro">
  <h2 class="heading">Linux server protection for everyone and everything</h2>
  <p class="intro-text">Cyber attacks happen. The question is, are you ready? For too many mid sized and small business the answer is no because they don’t think cyber protection is accessible or made for their needs. Even enterprises often are left unprotected by substandard endpoint protection or none at all. Velnastra protects Linux servers, web application servers, IoT devices and even Kestrabox containers. And, it just takes a couple of clicks for complete protection.</p>
  <div class="pills">
    <span class="pill">WAF Rules</span><span class="pill">Linux Servers</span><span class="pill">IoT Devices</span><span class="pill">Kestrabox Containers</span>
  </div>
</section>

<section class="services">
  <h2 class="heading">Our Services</h2>

  <div class="service" style="left:100px;top:125px">
    <svg width="60" height="60" viewBox="0 0 60 60" fill="none" stroke="#fff" stroke-width="2.5"><rect x="8" y="10" width="30" height="40" rx="3"/><line x1="8" y1="22" x2="38" y2="22"/><circle cx="23" cy="36" r="5"/><rect x="34" y="36" width="18" height="14" rx="2" fill="#fff"/><path d="M38 36 v-5 a5 5 0 0 1 10 0 v5"/></svg>
    <div><h3>Brindle Guard for Linux</h3><p>Nam libero tempore cum soluta no<br>bis est eligendi optio</p></div>
  </div>
  <div class="service" style="left:486px;top:125px">
    <svg width="60" height="60" viewBox="0 0 60 60" fill="none" stroke="#fff" stroke-width="2.5"><path d="M30 6 L50 14 V30 C50 42 41 50 30 54 C19 50 10 42 10 30 V14 Z"/><path d="M21 30 L28 37 L40 24"/></svg>
    <div><h3>QuellWarden Rules</h3><p>Nam libero tempore cum soluta no<br>bis est eligendi optio</p></div>
  </div>
  <div class="service" style="left:845px;top:125px">
    <svg width="60" height="60" viewBox="0 0 60 60" fill="none" stroke="#fff" stroke-width="2.5"><rect x="6" y="10" width="48" height="32" rx="2"/><rect x="14" y="17" width="14" height="18"/><rect x="32" y="17" width="14" height="18"/><line x1="20" y1="50" x2="40" y2="50"/><line x1="30" y1="42" x2="30" y2="50"/></svg>
    <div><h3>Shielded OS for Kestrabox</h3><p>Nam libero tempore cum soluta no<br>bis est eligendi optio</p></div>
  </div>
  <div class="service" style="left:100px;top:250px">
    <svg width="60" height="60" viewBox="0 0 60 60" fill="none" stroke="#fff" stroke-width="2.5"><rect x="8" y="8" width="44" height="12" rx="2"/><rect x="8" y="24" width="44" height="12" rx="2"/><rect x="8" y="40" width="44" height="12" rx="2"/><circle cx="16" cy="14" r="1.5" fill="#fff"/><circle cx="16" cy="30" r="1.5" fill="#fff"/><circle cx="16" cy="46" r="1.5" fill="#fff"/></svg>
    <div><h3>Velnastra Guarded Linux Kernels</h3><p>Nam libero tempore cum soluta no<br>bis est eligendi optio</p></div>
  </div>
  <div class="service" style="left:486px;top:250px">
    <svg width="60" height="60" viewBox="0 0 60 60" fill="none" stroke="#fff" stroke-width="2.5"><path d="M14 32 v-6 a16 16 0 0 1 32 0 v6"/><rect x="9" y="30" width="9" height="14" rx="3" fill="#fff"/><rect x="42" y="30" width="9" height="14" rx="3" fill="#fff"/><path d="M46 44 c0 6 -6 9 -12 9"/></svg>
    <div><h3>PRAVT - Commercial Support</h3><p>Nam libero tempore cum soluta no<br>bis est eligendi optio</p></div>
  </div>
  <div class="service" style="left:845px;top:250px">
    <svg width="60" height="60" viewBox="0 0 60 60" fill="none" stroke="#fff" stroke-width="2.5"><rect x="8" y="8" width="44" height="44" rx="3"/><line x1="8" y1="17" x2="52" y2="17"/><circle cx="30" cy="34" r="10"/><path d="M25 34 l4 4 l7 -7"/></svg>
    <div><h3>Shielded Apps for Kestrabox</h3><p>Nam libero tempore cum soluta no<br>bis est eligendi optio</p></div>
  </div>
</section>

<section class="clients">
  <h2 class="heading">More than 20,000 servers protected</h2>
  <div class="client-row">
    <div class="client"><span></span></div><div class="client"><span></span></div><div class="client"><span></span></div><div class="client"><span></span></div><div class="client"><span></span></div>
  </div>
  <div class="rule" style="top:284px"></div>
</section>

<section class="harden">
  <h2 class="heading">Harden your shell now</h2>
  <ul class="checks">
    <li><svg width="16" height="16" viewBox="0 0 16 16"><circle cx="8" cy="8" r="8" fill="#e5284a"/><path d="M4.5 8 L7 10.5 L11.5 5.5" stroke="#fff" stroke-width="1.8" fill="none"/></svg>At vero eos et accusamus et iusto odio dignissimos ducimus qui bla ditiis praesentium voluptatum deleniti atque.</li>
    <li><svg width="16" height="16" viewBox="0 0 16 16"><circle cx="8" cy="8" r="8" fill="#e5284a"/><path d="M4.5 8 L7 10.5 L11.5 5.5" stroke="#fff" stroke-width="1.8" fill="none"/></svg>Corrupti quos dolores et quas molestias excepturi sint occaecat</li>
    <li><svg width="16" height="16" viewBox="0 0 16 16"><circle cx="8" cy="8" r="8" fill="#e5284a"/><path d="M4.5 8 L7 10.5 L11.5 5.5" stroke="#fff" stroke-width="1.8" fill="none"/></svg>Opidita st non provident, similique sunt in culpa qui officia deserun</li>
    <li><svg width="16" height="16" viewBox="0 0 16 16"><circle cx="8" cy="8" r="8" fill="#e5284a"/><path d="M4.5 8 L7 10.5 L11.5 5.5" stroke="#fff" stroke-width="1.8" fill="none"/></svg>Mea ars mo, id est laborum et dolorum r harum quidem rerum</li>
    <li><svg width="16" height="16" viewBox="0 0 16 16"><circle cx="8" cy="8" r="8" fill="#e5284a"/><path d="M4.5 8 L7 10.5 L11.5 5.5" stroke="#fff" stroke-width="1.8" fill="none"/></svg>Set expedita libero tempore, cum soluta nobis est eligendiop nu cumom mi voluptas assumenda et repellendus</li>
  </ul>
  <div class="harden-video" role="img" aria-label="Aerial view of a road winding through dark forest">
    <div class="play"><svg width="26" height="28" viewBox="0 0 26 28"><path d="M4 2 L24 14 L4 26 Z" fill="#fff"/></svg></div>
  </div>
</section>

<section class="testimonial t1">
  <div class="testimonial-photo" role="img" aria-label="Tall glass office towers seen from below"></div>
  <div class="quote-mark">“</div>
  <p class="quote">“We trust our server security to Brindle Guard for Linux because it works. We’ve used it for years and it has been essential in keeping dark forces at bay.”</p>
  <p class="cite"><b>Dorian Vesk,</b> <i>Ember Quay</i></p>
  <svg class="arrow" style="left:200px" width="18" height="32" viewBox="0 0 18 32"><path d="M15 3 L3 16 L15 29" stroke="#fff" stroke-width="3" fill="none"/></svg>
  <svg class="arrow" style="left:982px" width="18" height="32" viewBox="0 0 18 32"><path d="M3 3 L15 16 L3 29" stroke="#fff" stroke-width="3" fill="none"/></svg>
</section>

<section class="containers">
  <h2 class="heading">Yes. You can secure Kestrabox containers</h2>
  <p>Kestrabox is the fastest growing application developer software in the world. But, people don’t realize that their containers are wide open to cyber attacks. Velnastra provides a secure OS kernel that is inherited by all containers on a single server. It’s easy to install, doesn’t impact performance and protects your containers against malicious attacks immediately.</p>
  <div class="rule" style="top:249px"></div>
</section>

<section class="customers">
  <h2 class="heading">Our Customers</h2>
  <div class="customer" style="left:178px">
    <svg width="100" height="105" viewBox="0 0 100 105" fill="#e5284a"><ellipse cx="42" cy="14" rx="34" ry="11"/><path d="M8 20 c0 8 68 8 68 0 v14 c0 8 -68 8 -68 0z"/><path d="M8 40 c0 8 68 8 68 0 v14 c0 8 -68 8 -68 0z"/><path d="M8 60 c0 8 68 8 68 0 v12 c0 8 -68 8 -68 0z"/><circle cx="74" cy="78" r="20"/><circle cx="74" cy="78" r="8" fill="#fff"/></svg>
    <span>Hosting Providers</span>
  </div>
  <div class="customer" style="left:456px">
    <svg width="100" height="105" viewBox="0 0 100 105" fill="#e5284a"><path d="M50 8 L92 30 L50 52 L8 30 Z"/><path d="M8 48 L50 70 L92 48 V58 L50 80 L8 58 Z"/><path d="M8 70 L50 92 L92 70 V80 L50 102 L8 80 Z"/></svg>
    <span>Enterprises</span>
  </div>
  <div class="customer" style="left:768px">
    <svg width="140" height="105" viewBox="0 0 140 105" fill="#e5284a"><path d="M4 30 L30 16 L44 46 L18 60 Z"/><path d="M136 30 L110 16 L96 46 L122 60 Z"/><path d="M36 30 L62 22 L82 30 L104 28 L112 50 L78 84 C72 90 64 88 60 82 L38 56 Z"/></svg>
    <span>Mid-sized &amp; Small Business</span>
  </div>
  <div class="customer" style="left:1058px">
    <svg width="100" height="105" viewBox="0 0 100 105" fill="none" stroke="#e5284a"><rect x="14" y="10" width="72" height="72" stroke-width="8"/><rect x="36" y="32" width="28" height="28" fill="#e5284a" stroke="none"/><line x1="10" y1="96" x2="90" y2="96" stroke-width="6"/></svg>
    <span>IoT OEMs</span>
  </div>
</section>

<section class="testimonial t2">
  <div class="testimonial-photo" role="img" aria-label="Hands typing on a laptop keyboard in low light"></div>
  <div class="quote-mark">“</div>
  <p class="quote">“Velnastra eliminated 90% of our shared server issues overnight. And, it saves us about four hours of staff time every day because it protects servers automatically.”</p>
  <p class="cite"><b>Marlo Trenholm,</b> <i>Copperfen</i></p>
  <svg class="arrow" style="left:200px" width="18" height="32" viewBox="0 0 18 32"><path d="M15 3 L3 16 L15 29" stroke="#fff" stroke-width="3" fill="none"/></svg>
  <svg class="arrow" style="left:982px" width="18" height="32" viewBox="0 0 18 32"><path d="M3 3 L15 16 L3 29" stroke="#fff" stroke-width="3" fill="none"/></svg>
</section>

<section class="blog">
  <h2 class="heading">Latest Blog</h2>
  <article class="feature-card">
    <div class="feature-img" role="img" aria-label="Hand holding a smartphone surrounded by floating connected-device graphics"></div>
    <h4>Finibus Bonorum et Malorum accusamus et iusto</h4>
    <div class="meta"><span><i></i>08/03/2017</span><span><i></i>John doe</span><span><i></i>0 comments</span></div>
  </article>

  <article class="post" style="top:145px">
    <div class="post-thumb" role="img" aria-label="Person working on a laptop at a desk" style="background:linear-gradient(135deg,#4d5058,#23262c)"></div>
    <h5>Finibus Bonorum et Malorum</h5>
    <div class="meta"><span><i></i>08/03/2017</span><span><i></i>John doe</span><span><i></i>0 comments</span></div>
    <p>Nam libero tempore, cum soluta nobis est eligendi optio cumque nihil impedit quo minus.</p>
  </article>
  <article class="post" style="top:300px">
    <div class="post-thumb" role="img" aria-label="Blue digital network graphic" style="background:linear-gradient(135deg,#9fd0f0,#2e6fae)"></div>
    <h5>Finibus Bonorum et Malorum</h5>
    <div class="meta"><span><i></i>08/03/2017</span><span><i></i>John doe</span><span><i></i>0 comments</span></div>
    <p>Nam libero tempore, cum soluta nobis est eligendi optio cumque nihil impedit quo minus.</p>
  </article>
  <article class="post" style="top:455px">
    <div class="post-thumb" role="img" aria-label="Padlock graphic over a dark blue screen" style="background:linear-gradient(135deg,#5d6f86,#1f2c3d)"></div>
    <h5>Finibus Bonorum et Malorum</h5>
    <div class="meta"><span><i></i>08/03/2017</span><span><i></i>John doe</span><span><i></i>0 comments</span></div>
    <p>Nam libero tempore, cum soluta nobis est eligendi optio cumque nihil impedit quo minus.</p>
  </article>
</section>

<section class="tweet">
  <span class="tweet-icon"></span>
  <p>Nemo enim ipsam voluptatem quia voluptas sit aspernatur aut odit aut fugit, sed quia consequuntur magni dolores eos qui ratione voluptatem sequi nesciunt neque porro quisquam</p>
</section>

<section class="contact">
  <h2 class="heading">Contact Us</h2>
  <h6 style="left:98px">Get In Touch:</h6>
  <div class="field" style="left:98px;top:175px;width:300px">Name</div>
  <div class="field" style="left:406px;top:175px;width:296px">Phone</div>
  <div class="field" style="left:98px;top:220px;width:604px">Email</div>
  <div class="field" style="left:98px;top:265px;width:604px;height:72px">Message</div>
  <div class="submit">SUBMIT</div>

  <h6 style="left:782px">Contact Information</h6>
  <div class="info" style="top:180px">
    <span class="info-icon"><svg width="12" height="16" viewBox="0 0 12 16"><path d="M6 0 C2.7 0 0 2.6 0 5.8 C0 10 6 16 6 16 S12 10 12 5.8 C12 2.6 9.3 0 6 0Z" fill="#e5284a"/><circle cx="6" cy="6" r="2.2" fill="#fff"/></svg></span>
    <span>Calle Brisna 14, Ventoral,<br>40210 Spain</span>
  </div>
  <div class="info" style="top:240px">
    <span class="info-icon"><svg width="14" height="14" viewBox="0 0 14 14"><path d="M3 0 L5.5 3.5 L4 5.2 C5 7.3 6.7 9 8.8 10 L10.5 8.5 L14 11 L12.5 14 C6 13.5 0.5 8 0 1.5Z" fill="#e5284a"/></svg></span>
    <span>1 555 014 2290</span>
  </div>
  <div class="info" style="top:298px">
    <span class="info-icon"><svg width="16" height="12" viewBox="0 0 16 12"><rect x="0" y="0" width="16" height="12" rx="1.5" fill="#e5284a"/><path d="M1 1.5 L8 7 L15 1.5" stroke="#fff" stroke-width="1.4" fill="none"/></svg></span>
    <span>info@velnastra.com</span>
  </div>
  <div class="socials">
    <span style="background:#2b4f9a"></span><span style="background:#2196e8"></span><span style="background:#e5284a"></span><span style="background:#8a6a4a"></span>
  </div>
  <div class="rule" style="top:424px"></div>
</section>

<footer class="site-footer">
  <p>Copyrights © 2017, Velnastra. All Rights Reserved.</p>
</footer>

</body>
</html>
```